Tallowreed Advisory Partners Business Card Design

We have the logo we just need someone to design a modern business card design.

Name: Desmond Munkalt
Phone: 3055550148
Mobile: 9175550193
Web:www.tallowreedadvisory.example
email: dmunkalt@tallowreedadvisory.example
Company: Tallowreed Advisory Partners
Title: CEO

Address: 718 Quillmore Ave, Miami, Florida 33190

Target Market(s)

companies over 100 employees

Industry/Entity Type

Business

```html
<!DOCTYPE html>
<html lang="en">
<head>
<meta charset="utf-8">
<title>Tallowreed Advisory Partners – Business Card</title>
<link rel="stylesheet" href="https://fonts.googleapis.com/css2?family=Open+Sans:wght@400;600;700&display=swap">
<style>
  :root {
    --page-bg: #e4e4e4;
    --card-white: #f7f7f7;
    --card-black: #1c1c1d;
    --brand-blue: #2f45b5;
    --ink-dark: #262626;
    --ink-light: #f2f2f2;
    --ink-muted: #cfcfcf;
    --pattern-light: #9a9a9a;
    --pattern-dark: #4a4a4a;
  }
  * { box-sizing: border-box; margin: 0; padding: 0; }
  html, body { width: 1200px; height: 1200px; overflow: hidden; }
  body {
    background: var(--page-bg);
    font-family: "Open Sans", sans-serif;
    display: flex;
    flex-direction: column;
    align-items: center;
    justify-content: center;
    gap: 60px;
  }
  .card {
    position: relative;
    width: 700px;
    height: 400px;
    overflow: hidden;
    box-shadow: 0 6px 18px rgba(0,0,0,0.18);
  }

  /* Front */
  .card-front { background: var(--card-white); }
  .wire-texture {
    position: absolute; left: 0; width: 100%;
    background: linear-gradient(135deg, var(--pattern-light), var(--pattern-dark) 50%, var(--pattern-light));
  }
  .wire-texture.top { top: 0; height: 62px; }
  .wire-texture.bottom { bottom: 0; height: 150px; }
  .front-logo {
    position: absolute; top: 90px; left: 0; width: 100%;
    display: flex; flex-direction: column; align-items: center; gap: 14px;
  }
  .logo-dot {
    width: 66px; height: 66px; border-radius: 50%;
    background: var(--brand-blue);
  }
  .front-logo .logo-name {
    font-size: 30px; font-weight: 700; letter-spacing: 1px;
    color: var(--ink-dark);
  }

  /* Back */
  .card-back { background: var(--card-black); color: var(--ink-light); }
  .accent-bar {
    position: absolute; left: 0; top: 96px;
    width: 110px; height: 40px; background: var(--brand-blue);
  }
  .back-logo {
    position: absolute; left: 125px; top: 58px; width: 240px;
    display: flex; flex-direction: column; align-items: center; gap: 10px;
  }
  .back-logo .logo-dot { width: 48px; height: 48px; }
  .back-logo .logo-name {
    font-size: 24px; font-weight: 700; letter-spacing: 1px;
    color: var(--ink-light);
  }
  .name-band {
    position: absolute; right: 0; top: 168px;
    width: 360px; height: 66px; background: var(--brand-blue);
    padding: 10px 22px 0 0; text-align: right;
  }
  .person-name { font-size: 22px; font-weight: 700; line-height: 1.2; }
  .person-title { font-size: 13px; font-weight: 400; }
  .contact-list {
    position: absolute; left: 34px; top: 258px;
    list-style: none; font-size: 14.5px; color: var(--ink-muted);
    display: flex; flex-direction: column; gap: 6px;
  }
  .phone-list {
    position: absolute; left: 470px; top: 282px;
    list-style: none; font-size: 17px; color: var(--ink-muted);
    display: flex; flex-direction: column; gap: 4px;
  }
  .contact-list li, .phone-list li { display: flex; align-items: center; gap: 10px; }
  .icon { width: 13px; height: 13px; flex: none; fill: none; stroke: var(--ink-muted); stroke-width: 1.6; }
  .divider {
    position: absolute; left: 445px; top: 272px;
    width: 1px; height: 70px; background: var(--ink-muted);
  }
</style>
</head>
<body>

  <section class="card card-front" aria-label="Card front">
    <div class="wire-texture top" role="img" aria-label="Tangled black wire pattern"></div>
    <div class="front-logo">
      <span class="logo-dot"></span>
      <span class="logo-name">Tallowreed Advisory Partners</span>
    </div>
    <div class="wire-texture bottom" role="img" aria-label="Tangled black wire pattern"></div>
  </section>

  <section class="card card-back" aria-label="Card back">
    <div class="accent-bar"></div>
    <div class="back-logo">
      <span class="logo-dot"></span>
      <span class="logo-name">Tallowreed</span>
    </div>

    <div class="name-band">
      <p class="person-name">Desmond Munkalt</p>
      <p class="person-title">CEO</p>
    </div>

    <ul class="contact-list">
      <li>
        <svg class="icon" viewBox="0 0 14 14"><path d="M7 13 C3 8 2.5 6.5 2.5 5 A4.5 4.5 0 0 1 11.5 5 C11.5 6.5 11 8 7 13Z"/><circle cx="7" cy="5" r="1.5"/></svg>
        718 Quillmore Ave, Miami, Florida 33190
      </li>
      <li>
        <svg class="icon" viewBox="0 0 14 14"><rect x="1" y="3" width="12" height="8"/><path d="M1 3 L7 8 L13 3"/></svg>
        dmunkalt@tallowreedadvisory.example
      </li>
      <li>
        <svg class="icon" viewBox="0 0 14 14"><circle cx="7" cy="7" r="6"/><path d="M1 7 H13 M7 1 C4 4 4 10 7 13 C10 10 10 4 7 1"/></svg>
        www.tallowreedadvisory.example
      </li>
    </ul>

    <div class="divider"></div>

    <ul class="phone-list">
      <li>
        <svg class="icon" viewBox="0 0 14 14"><path d="M3 1 L5.5 1 L6.5 4 L5 5.5 C6 7.5 6.5 8 8.5 9 L10 7.5 L13 8.5 L13 11 C13 12 12 13 11 13 C6 13 1 8 1 3 C1 2 2 1 3 1Z"/></svg>
        3055550148
      </li>
      <li>
        <svg class="icon" viewBox="0 0 14 14"><rect x="3.5" y="1" width="7" height="12" rx="1"/><path d="M6 11 H8"/></svg>
        9175550193
      </li>
    </ul>
  </section>

</body>
</html>
```